Business Cards & Letterhead etc.
Would like our Business Cards designed off our Logo
Professional
Dale Fenwick
PO Box 61309
Alder Falls, OH 43987
fenwickd@quellbridgeco.com
www.quellbridgeco.com
I would like the business cards to be designed so i can later alter the contact info for multiple people. Anything in Adobe is fine.

```html
<!DOCTYPE html>
<html lang="en">
<head>
<meta charset="utf-8">
<title>Quell IT Group – Business Cards</title>
<link rel="stylesheet" href="https://fonts.googleapis.com/css2?family=Arimo:wght@400;700&display=swap">
<style>
  :root {
    --page-bg: #e9e9eb;
    --card-dark: #1c1d20;
    --card-dark-2: #0f1012;
    --accent-blue: #1d8fe0;
    --text-white: #ffffff;
    --text-grey: #b9bcc1;
    --text-panel: #f4f5f7;
    --rule: #ffffff;
  }
  * { box-sizing: border-box; margin: 0; padding: 0; }
  html, body {
    width: 1200px; height: 974px; overflow: hidden;
    background: var(--page-bg);
    font-family: "Arimo", Arial, sans-serif;
  }
  .canvas { position: relative; width: 1200px; height: 974px; }

  .card {
    position: absolute;
    width: 720px; height: 412px;
    border-radius: 18px;
    overflow: hidden;
    background: radial-gradient(ellipse at 65% 40%, var(--card-dark) 0%, var(--card-dark-2) 100%);
    box-shadow: 0 14px 34px rgba(0,0,0,0.35);
  }
  .card--front { left: 60px; top: 60px; }
  .card--back { left: 420px; top: 502px; }

  .card__art { position: absolute; inset: 0; width: 100%; height: 100%; }

  .brand {
    position: absolute;
    display: flex; align-items: center; gap: 14px;
  }
  .brand__mark {
    border-radius: 50%;
    background: radial-gradient(circle at 35% 30%, #f2f3f5, #7d8187 70%, #4a4d52);
    flex: none;
  }
  .brand__name {
    color: var(--text-white);
    font-weight: 700;
    text-transform: uppercase;
    line-height: 1;
  }
  .card--front .brand { left: 326px; top: 34px; }
  .card--front .brand__mark { width: 66px; height: 66px; }
  .card--front .brand__name { font-size: 38px; letter-spacing: 1px; }
  .brand__name small { display: block; font-size: 22px; margin-top: 6px; letter-spacing: 2px; }

  .person {
    position: absolute; left: 360px; top: 216px; width: 290px;
    text-align: center;
  }
  .person__name { color: var(--accent-blue); font-size: 31px; font-weight: 700; }
  .person__role { color: var(--text-grey); font-size: 18px; margin-top: 4px; }

  .contact {
    position: absolute; left: 22px; top: 156px;
    color: var(--text-panel); font-size: 16px; line-height: 1.3;
  }
  .contact__rule {
    width: 150px; border-top: 3px dotted var(--rule);
    margin: 12px 0 10px;
  }
  .contact__list { list-style: none; }
  .contact__list li { display: flex; align-items: center; gap: 8px; font-size: 15px; line-height: 1.45; }
  .contact__list svg { width: 14px; height: 14px; fill: var(--text-panel); flex: none; }

  .site {
    position: absolute; color: var(--text-white); font-weight: 700;
  }
  .card--front .site { left: 22px; bottom: 22px; font-size: 21px; }
  .card--back .site { right: 40px; bottom: 124px; font-size: 17px; }

  .card--back .brand { right: 150px; top: 214px; gap: 0; }
  .card--back .brand__mark { width: 52px; height: 52px; }
</style>
</head>
<body>
<main class="canvas">

  <section class="card card--front" aria-label="Business card front">
    <svg class="card__art" viewBox="0 0 720 412" aria-hidden="true">
      <defs>
        <linearGradient id="panelShade" x1="0" y1="0" x2="1" y2="1">
          <stop offset="0" stop-color="#d3d5d8"/>
          <stop offset="0.55" stop-color="#a3a6ab"/>
          <stop offset="1" stop-color="#7c7f85"/>
        </linearGradient>
        <linearGradient id="swoosh" x1="0" y1="0" x2="0" y2="1">
          <stop offset="0" stop-color="#5cc1ff"/>
          <stop offset="1" stop-color="#0f6fb8"/>
        </linearGradient>
      </defs>
      <path d="M0 0 H300 C215 110 225 280 345 412 H0 Z" fill="#3a3d42"/>
      <path d="M0 0 H278 C195 110 205 280 322 412 H0 Z" fill="url(#panelShade)"/>
      <path d="M300 0 C215 110 225 280 345 412" fill="none" stroke="url(#swoosh)" stroke-width="9"/>
    </svg>

    <div class="brand">
      <span class="brand__mark"></span>
      <span class="brand__name">Quell<small>IT Group</small></span>
    </div>

    <div class="person">
      <p class="person__name">Dale Fenwick</p>
      <p class="person__role">Owner</p>
    </div>

    <div class="contact">
      <p>PO Box 61309</p>
      <p>Alder Falls, OH 43987</p>
      <div class="contact__rule"></div>
      <ul class="contact__list">
        <li><svg viewBox="0 0 16 16"><path d="M3 1h3l1.5 4-2 1.3a9 9 0 0 0 4.2 4.2L11 8.5l4 1.5v3a2 2 0 0 1-2 2A12 12 0 0 1 1 3a2 2 0 0 1 2-2z"/></svg>866-555-0142</li>
        <li><svg viewBox="0 0 16 16"><rect x="4" y="1" width="8" height="14" rx="1.5"/></svg>555-555-0187</li>
        <li><svg viewBox="0 0 16 16"><rect x="1" y="5" width="14" height="9" rx="1"/><rect x="4" y="1" width="8" height="4"/></svg>866-555-0163</li>
        <li><svg viewBox="0 0 16 16"><path d="M1 3h14v10H1z M1 3l7 5 7-5" fill="none" stroke="#f4f5f7" stroke-width="1.6"/></svg>fenwickd@quellbridgeco.com</li>
      </ul>
    </div>

    <p class="site">www.quellbridgeco.com</p>
  </section>

  <section class="card card--back" aria-label="Business card back">
    <div class="brand">
      <span class="brand__mark"></span>
    </div>
    <p class="site">www.quellbridgeco.com</p>
  </section>

</main>
</body>
</html>
```